Shopify Design for wedding invitations

We are a greeting card manufactory, special in wedding invitation
I need a shopify website for our wedding invitation brand. (Lovonna), atttach you can find our logo.
We are looking for someone to create a modern and clean looking e-commerce store for our wedding invitation through Shopify. We need some life, professionalism and style put into our site. We will have a variety serie of products : laser cut wedding invitation, popup wedding invitaiton, vintage wedding invitation, handmade wedding invitation, printing invitation, Custom wedding cards, wedding stationery (including favor box, table card, place card, escort card, number card), Thank you card. our online store requires easy navigation to categories divided by product type.

our market is , Eourpe and USA,
please choose a good color for it.
you can go to our website: www.bluepinecrafts.com and check our product.
also you can go to Shopvane 4 new items.
https://www.shopvane.com/dp/K47T8M2Q61?ref=myi_title_dp

Designs look the same

Target Market(s)

Europe and USA

Industry/Entity Type

wedding

Number of Pages Required

1 page

Requirements
Must have
• Logo, 3 banners than can be changed each 3-5 seconds.
Nice to have
• nice icon and font, beautiful color,

```html
<!DOCTYPE html>
<html lang="en">
<head>
<meta charset="utf-8">
<title>Lovonna – Wedding Invitations</title>
<link href="https://fonts.googleapis.com/css2?family=Poppins:wght@400;500;600;700&family=Satisfy&family=Dancing+Script:wght@600&display=swap" rel="stylesheet">
<style>
:root{
  --green:#6c9c2f;
  --brown:#5b2c1f;
  --red:#d0021b;
  --ink:#333333;
  --muted:#555555;
  --grey-bg:#f3f3f3;
  --footer:#343434;
  --footer-deep:#262626;
  --white:#ffffff;
  --script:'Satisfy','Dancing Script',cursive;
}
*{box-sizing:border-box;margin:0;padding:0}
html,body{width:1200px;height:4576px;overflow:hidden}
body{position:relative;font-family:'Poppins',sans-serif;color:var(--ink);background:var(--white)}
.abs{position:absolute}
.photo{position:absolute}

.topbar{left:0;top:0;width:1200px;height:57px;background:var(--green);color:var(--white);font-size:18px}
.topbar .phone{left:68px;top:15px;font-weight:600;display:flex;gap:10px;align-items:center}
.topbar .ship{left:282px;top:15px;display:flex;gap:10px;align-items:center}
.topbar .icons{right:74px;top:17px;display:flex;gap:26px;align-items:center;font-size:14px}

.nav{left:0;top:57px;width:1200px;height:108px;background:var(--white)}
.logo{font-family:var(--script);font-weight:400;font-size:62px;color:var(--brown);line-height:1;white-space:nowrap}
.nav .logo{left:98px;top:20px}
.menu{left:336px;top:40px;display:flex;font-size:17px;font-weight:500}
.menu a{color:var(--ink);text-decoration:none;margin-right:40px}
.menu a:last-child{margin-right:0}
.menu a.active{color:var(--red)}

.hero{left:0;top:165px;width:1200px;height:581px;background:
  radial-gradient(ellipse 260px 200px at 640px 300px,#b58a5c,transparent 70%),
  radial-gradient(ellipse 200px 160px at 380px 120px,#d8d0c4,transparent 70%),
  linear-gradient(135deg,#3d2216,#5e3824 45%,#4a2a1a)}
.hero-title{left:0;width:1200px;top:132px;text-align:center;font-family:var(--script);font-size:108px;color:var(--white);line-height:1;white-space:nowrap}
.hero-sub{left:0;width:1200px;top:257px;text-align:center;font-size:36px;color:var(--white);font-weight:500;line-height:43px}
.btn{display:flex;align-items:center;justify-content:center;background:var(--green);color:var(--white);font-weight:600}
.hero .btn{left:511px;top:380px;width:178px;height:53px;font-size:21px}
.dots{left:511px;top:517px;display:flex;gap:10px}
.dots span{width:36px;height:4px;background:var(--white)}
.dots span:first-child{background:var(--red)}

.tile-label{font-family:var(--script);color:var(--white);font-size:33px;line-height:37px;white-space:nowrap}
.big-label{color:var(--brown)}
.view-all{left:470px;top:1374px;width:261px;height:69px;font-size:22px}

.band{left:0;width:1200px}
.sec-title{font-family:var(--script);color:var(--brown);font-size:46px;line-height:1;white-space:nowrap}
.arrows{display:flex;gap:14px}
.card{position:absolute;width:242px;text-align:center}
.card .img{height:200px}
.card h3{font-size:18px;font-weight:600;margin-top:20px;color:var(--ink)}
.card p{font-size:15px;margin-top:2px;color:var(--muted);white-space:nowrap}
.card .price{color:var(--red);font-weight:600;font-size:18px;margin-top:2px}
.card .cart{display:inline-block;margin-top:14px;width:128px;height:40px;line-height:37px;border:1.5px solid var(--green);color:var(--green);font-size:15px;font-weight:500}

.about-text{left:616px;top:2770px;width:510px;font-size:16px;line-height:29.5px;color:var(--muted)}

.news-box{background:var(--white);text-align:center;padding-top:26px}
.news-box .date{color:var(--red);font-weight:600;font-size:18px}
.news-box .head{font-size:22px;line-height:32px;margin-top:4px;color:var(--ink)}
.news-box .more{font-size:15px;font-weight:600;margin-top:12px;color:var(--brown)}

.footer{left:0;top:4106px;width:1200px;height:372px;background:var(--footer);color:var(--white)}
.footer .logo{color:var(--white);left:75px;top:24px;font-size:58px}
.email{left:286px;top:41px;width:461px;height:44px;border:1px solid #9a9a9a;background:var(--white);color:var(--ink);font-size:15px;padding:11px 18px}
.signup{left:760px;top:41px;width:101px;height:44px;font-size:15px}
.social{left:888px;top:49px;display:flex;gap:24px}
.social span{width:28px;height:28px;border-radius:50%;background:var(--white)}
.footer .rule{left:0;top:115px;width:1200px;height:1px;background:#4a4a4a}
.col h4{font-family:var(--script);font-weight:400;font-size:30px;color:var(--white);margin-bottom:12px;line-height:1.2}
.col ul{list-style:none;font-size:14.5px;line-height:37px}
.bottom{left:0;top:4478px;width:1200px;height:98px;background:var(--footer-deep);color:var(--white);font-size:14px}
.cards{right:74px;top:34px;display:flex;gap:8px}
.cards span{width:46px;height:30px;border-radius:3px}
</style>
</head>
<body>

<div class="abs topbar">
  <div class="abs phone">
    <svg width="18" height="18" viewBox="0 0 24 24" fill="#fff"><path d="M6.6 10.8a15 15 0 0 0 6.6 6.6l2.2-2.2c.3-.3.7-.4 1-.2 1.1.4 2.3.6 3.6.6.6 0 1 .4 1 1V20c0 .6-.4 1-1 1A17 17 0 0 1 3 4c0-.6.4-1 1-1h3.5c.6 0 1 .4 1 1 0 1.3.2 2.5.6 3.6.1.3 0 .7-.2 1z"/></svg>
    +86 13900482715
  </div>
  <div class="abs ship">
    <svg width="24" height="18" viewBox="0 0 24 18" fill="#fff"><rect x="0" y="2" width="14" height="10"/><path d="M14 5h5l4 4v3h-9z"/><circle cx="5" cy="14" r="2.5"/><circle cx="18" cy="14" r="2.5"/></svg>
    Free Shipping
  </div>
  <div class="abs icons">
    <svg width="18" height="18" viewBox="0 0 24 24" fill="none" stroke="#fff" stroke-width="3"><circle cx="10" cy="10" r="6"/><path d="M15 15l6 6"/></svg>
    <svg width="18" height="18" viewBox="0 0 24 24" fill="#fff"><circle cx="12" cy="7" r="5"/><path d="M2 22c0-6 4-9 10-9s10 3 10 9z"/></svg>
    <svg width="18" height="18" viewBox="0 0 24 24" fill="#fff"><path d="M12 21L3 12a5 5 0 0 1 9-6 5 5 0 0 1 9 6z"/></svg>
    <span style="display:flex;gap:4px;align-items:center"><svg width="20" height="18" viewBox="0 0 24 20" fill="#fff"><path d="M1 6h22l-3 13H4z"/><path d="M7 6l4-5M17 6l-4-5" stroke="#fff" stroke-width="2"/></svg>(0)</span>
  </div>
</div>

<div class="abs nav">
  <div class="abs logo">Lovonna</div>
  <nav class="abs menu">
    <a class="active">Home</a><a>About Us</a><a>Products</a><a>Shop</a><a>Specials</a><a>Reviews</a><a>News</a><a>Contact Us</a>
  </nav>
</div>

<section class="abs hero" role="img" aria-label="Laser cut lace wedding invitations with kraft envelopes and twine on a dark wooden table">
  <div class="abs hero-title">Welcome to Lovonna</div>
  <div class="abs hero-sub">Elegant Laser cut wedding card printable<br>invitation paper with envelope</div>
  <div class="abs btn">Shop Now</div>
  <div class="abs dots"><span></span><span></span><span></span><span></span></div>
</section>

<div class="photo" style="left:75px;top:818px;width:511px;height:496px;background:radial-gradient(ellipse 180px 220px at 210px 220px,#3fae95,transparent 75%),radial-gradient(circle at 460px 90px,#e7a8c4,transparent 30%),linear-gradient(135deg,#ececec,#f7f7f7 60%,#eee6e8)" role="img" aria-label="Teal laser cut wedding invitation beside pink flowers">
  <div class="abs tile-label big-label" style="left:20px;top:402px">Laser Cut Wedding<br>Invitation</div>
</div>
<div class="photo" style="left:602px;top:818px;width:254px;height:240px;background:radial-gradient(ellipse 90px 100px at 140px 110px,#c19b5a,transparent 75%),linear-gradient(135deg,#5c3522,#8a5e3c 50%,#4a2a1a)" role="img" aria-label="Gold lace pocket invitation on kraft envelope">
  <div class="abs tile-label" style="left:14px;top:154px">Popup Wedding<br>Invitation</div>
</div>
<div class="photo" style="left:872px;top:818px;width:254px;height:240px;background:radial-gradient(ellipse 100px 100px at 150px 100px,#eeeae3,transparent 75%),radial-gradient(circle at 240px 20px,#8a6fa8,transparent 25%),linear-gradient(135deg,#5c3522,#7a4c30)" role="img" aria-label="White vintage lace invitation with lavender">
  <div class="abs tile-label" style="left:14px;top:154px">Vintage Wedding<br>Invitation</div>
</div>
<div class="photo" style="left:602px;top:1076px;width:524px;height:238px;background:radial-gradient(ellipse 160px 130px at 320px 120px,#dcc39a,transparent 75%),linear-gradient(135deg,#5c3522,#a57b4f 40%,#5c3522)" role="img" aria-label="Kraft gatefold popup invitation with floral laser cut doors">
  <div class="abs tile-label" style="left:14px;top:150px">Popup Wedding<br>Invitation</div>
</div>
<div class="abs btn view-all">View All Products</div>

<section class="abs band" style="top:1535px;height:545px;background:var(--grey-bg)">
  <div class="abs sec-title" style="left:73px;top:56px">Featured Products</div>
  <div class="abs arrows" style="left:1048px;top:70px">
    <svg width="30" height="30" viewBox="0 0 30 30"><circle cx="15" cy="15" r="15" fill="#999"/><path d="M18 8l-7 7 7 7M11 15h10" stroke="#fff" stroke-width="3" fill="none"/></svg>
    <svg width="30" height="30" viewBox="0 0 30 30"><circle cx="15" cy="15" r="15" fill="var(--brown)"/><path d="M12 8l7 7-7 7M19 15H9" stroke="#fff" stroke-width="3" fill="none"/></svg>
  </div>
  <div class="card" style="left:75px;top:139px"><div class="img" role="img" aria-label="Gold lace invitation on kraft envelope" style="background:radial-gradient(ellipse 80px 70px at 140px 110px,#b9954f,transparent 80%),linear-gradient(135deg,#5c3522,#a27a4e)"></div><h3>Product Heading</h3><p>Nemo enim ipsam voluptatem</p><div class="price">$8.99</div><div class="cart">Add to Cart</div></div>
  <div class="card" style="left:344px;top:139px"><div class="img" role="img" aria-label="White lace invitation with ribbon" style="background:radial-gradient(ellipse 110px 100px at 130px 100px,#f1eee8,transparent 80%),linear-gradient(135deg,#5c3522,#8a5e3c)"></div><h3>Product Heading</h3><p>Nemo enim ipsam voluptatem</p><div class="price">$8.99</div><div class="cart">Add to Cart</div></div>
  <div class="card" style="left:614px;top:139px"><div class="img" role="img" aria-label="Navy invitation with gold lace" style="background:radial-gradient(ellipse 80px 90px at 150px 100px,#24305c,transparent 80%),linear-gradient(135deg,#a07850,#6b4129)"></div><h3>Product Heading</h3><p>Nemo enim ipsam voluptatem</p><div class="price">$8.99</div><div class="cart">Add to Cart</div></div>
  <div class="card" style="left:884px;top:139px"><div class="img" role="img" aria-label="Burgundy laser cut invitation" style="background:radial-gradient(ellipse 80px 90px at 150px 100px,#7a2d3c,transparent 80%),linear-gradient(135deg,#a07850,#6b4129)"></div><h3>Product Heading</h3><p>Nemo enim ipsam voluptatem</p><div class="price">$8.99</div><div class="cart">Add to Cart</div></div>
</section>

<section class="abs band" style="top:2080px;height:540px">
  <div class="abs sec-title" style="left:73px;top:44px">Best Sellers</div>
  <div class="abs arrows" style="left:1048px;top:53px">
    <svg width="30" height="30" viewBox="0 0 30 30"><circle cx="15" cy="15" r="15" fill="#999"/><path d="M18 8l-7 7 7 7M11 15h10" stroke="#fff" stroke-width="3" fill="none"/></svg>
    <svg width="30" height="30" viewBox="0 0 30 30"><circle cx="15" cy="15" r="15" fill="var(--brown)"/><path d="M12 8l7 7-7 7M19 15H9" stroke="#fff" stroke-width="3" fill="none"/></svg>
  </div>
  <div class="card" style="left:75px;top:121px"><div class="img" role="img" aria-label="Kraft gatefold floral invitation" style="background:radial-gradient(ellipse 90px 80px at 140px 100px,#d7bd95,transparent 80%),linear-gradient(135deg,#5c3522,#9c744a)"></div><h3>Product Heading</h3><p>Nemo enim ipsam voluptatem</p><div class="price">$8.99</div><div class="cart">Add to Cart</div></div>
  <div class="card" style="left:344px;top:121px"><div class="img" role="img" aria-label="White vintage invitation with flowers" style="background:radial-gradient(ellipse 90px 90px at 130px 100px,#eae6df,transparent 80%),radial-gradient(circle at 230px 20px,#8a6fa8,transparent 25%),linear-gradient(135deg,#5c3522,#7a4c30)"></div><h3>Product Heading</h3><p>Nemo enim ipsam voluptatem</p><div class="price">$8.99</div><div class="cart">Add to Cart</div></div>
  <div class="card" style="left:614px;top:121px"><div class="img" role="img" aria-label="Red laser cut invitation" style="background:radial-gradient(ellipse 90px 110px at 130px 100px,#c81e2a,transparent 80%),linear-gradient(135deg,#d9d9d9,#eeeeee)"></div><h3>Product Heading</h3><p>Nemo enim ipsam voluptatem</p><div class="price">$8.99</div><div class="cart">Add to Cart</div></div>
  <div class="card" style="left:884px;top:121px"><div class="img" role="img" aria-label="Gold lace pocket invitation" style="background:radial-gradient(ellipse 90px 70px at 140px 110px,#b9954f,transparent 80%),linear-gradient(135deg,#5c3522,#8a5e3c)"></div><h3>Product Heading</h3><p>Nemo enim ipsam voluptatem</p><div class="price">$8.99</div><div class="cart">Add to Cart</div></div>
</section>

<section class="abs band" style="top:2620px;height:483px;background:var(--grey-bg)"></section>
<div class="abs" style="left:75px;top:2707px;width:328px;height:311px;background:var(--green)"></div>
<div class="photo" style="left:90px;top:2723px;width:496px;height:312px;background:radial-gradient(ellipse 150px 140px at 220px 170px,#d6b98e,transparent 80%),linear-gradient(135deg,#6e2634,#5c3522 50%,#4a2a1a)" role="img" aria-label="Gold laser cut floral invitation on a wooden desk with pen"></div>
<div class="abs sec-title" style="left:616px;top:2694px">About Us</div>
<p class="abs about-text">Nemo enim ipsam voluptatem quia voluptas sit aspernatur aut odit aut fugit, sed quia consequuntur magni dolores eos qui ratione voluptatem sequi nesciunt. Neque porro quisquam est, qui dolorem ipsum quia dolor sit amet, consectetur, enim ad minima veniam, quis nostrum exercitationem ullam corporis suscipit laboriosam, nisi ut aliquid.</p>
<div class="abs btn" style="left:616px;top:2979px;width:167px;height:56px;font-size:19px">Read More</div>

<div class="abs sec-title" style="left:70px;top:3164px">Latest News</div>
<div class="abs arrows" style="left:1048px;top:3183px">
  <svg width="30" height="30" viewBox="0 0 30 30"><circle cx="15" cy="15" r="15" fill="#999"/><path d="M18 8l-7 7 7 7M11 15h10" stroke="#fff" stroke-width="3" fill="none"/></svg>
  <svg width="30" height="30" viewBox="0 0 30 30"><circle cx="15" cy="15" r="15" fill="var(--brown)"/><path d="M12 8l7 7-7 7M19 15H9" stroke="#fff" stroke-width="3" fill="none"/></svg>
</div>
<div class="photo" style="left:75px;top:3254px;width:511px;height:310px;background:radial-gradient(ellipse 120px 40px at 150px 170px,#2f8d9a,transparent 80%),radial-gradient(ellipse 120px 90px at 380px 180px,#e9c9b8,transparent 80%),linear-gradient(135deg,#ebe8ec,#d9d5d9)" role="img" aria-label="Hands trimming a laser cut lace card with scissors"></div>
<div class="photo" style="left:614px;top:3254px;width:512px;height:310px;background:radial-gradient(circle at 40% 40%,#f6f2ea,#d8d0c2)" role="img" aria-label="Close-up of pearl white embossed lace invitation"></div>
<div class="abs news-box" style="left:94px;top:3507px;width:472px;height:167px"><div class="date">Jun15, 2022</div><div class="head">Sed ut perspiciatis unde omnis iste<br>natus error sit voluptatem</div><div class="more">Read More</div></div>
<div class="abs news-box" style="left:634px;top:3507px;width:472px;height:167px"><div class="date">Jun15, 2022</div><div class="head">Sed ut perspiciatis unde omnis iste<br>natus error sit voluptatem</div><div class="more">Read More</div></div>

<section class="abs band" style="top:3722px;height:384px;background:#f5f5f5">
  <div class="abs sec-title" style="left:0;width:1200px;text-align:center;top:56px">Instagram</div>
  <div class="photo" style="left:75px;top:140px;width:261px;height:180px;background:radial-gradient(ellipse 80px 80px at 150px 90px,#7a2d3c,transparent 80%),linear-gradient(135deg,#a07850,#6b4129)" role="img" aria-label="Burgundy invitation"></div>
  <div class="photo" style="left:338px;top:140px;width:261px;height:180px;background:radial-gradient(ellipse 90px 90px at 130px 90px,#c81e2a,transparent 80%),linear-gradient(135deg,#dcdcdc,#eeeeee)" role="img" aria-label="Red laser cut invitation"></div>
  <div class="photo" style="left:602px;top:140px;width:259px;height:180px;background:radial-gradient(ellipse 100px 80px at 130px 90px,#efebe4,transparent 80%),linear-gradient(135deg,#5c3522,#8a5e3c)" role="img" aria-label="White lace invitation"></div>
  <div class="photo" style="left:863px;top:140px;width:261px;height:180px;background:radial-gradient(ellipse 80px 90px at 160px 90px,#24305c,transparent 80%),linear-gradient(135deg,#a07850,#6b4129)" role="img" aria-label="Navy and gold invitation"></div>
</section>

<footer class="abs footer">
  <div class="abs logo">Lovonna</div>
  <div class="abs email">Email Address</div>
  <div class="abs btn signup">SIGN UP</div>
  <div class="abs social"><span></span><span></span><span></span><span></span><span></span></div>
  <div class="abs rule"></div>
  <div class="abs col" style="left:75px;top:135px"><h4>Navigation</h4>
    <div style="display:flex;gap:55px"><ul><li>Home</li><li>About Us</li><li>Products</li><li>Shop</li></ul><ul style="margin-top:-6px"><li>Specials</li><li>Reviews</li><li>News</li><li>Contact Us</li></ul></div>
  </div>
  <div class="abs col" style="left:360px;top:135px"><h4>Products</h4><ul style="margin-top:-6px"><li>Laser cut wedding invitation,</li><li>Popup wedding invitation</li><li>Vintage wedding invitation</li><li>Handmade wedding invitation</li></ul></div>
  <div class="abs col" style="left:666px;top:135px"><h4>My Account</h4><ul style="margin-top:-6px"><li>Sed ut perspiciatis</li><li>Unde omnis iste</li><li>Natus error sit</li><li>Voluptatem</li></ul></div>
  <div class="abs col" style="left:884px;top:135px"><h4>Address</h4>
    <p style="font-size:14.5px;line-height:27px;margin-top:-6px">Unit 12, 3rd Floor, Maple Court,<br>Lanting Road, Fernhill,<br>480215</p>
    <p style="font-size:14.5px;margin-top:10px">☎&nbsp;&nbsp;&nbsp;+86 13900482715</p>
    <p style="font-size:14.5px;margin-top:12px">✉&nbsp;&nbsp;&nbsp;info@lovonnacards.com</p>
  </div>
</footer>
<div class="abs bottom">
  <div class="abs" style="left:75px;top:38px">© Copyright 2022 CompanyName All Rights Reserved</div>
  <div class="abs cards"><span style="background:#e6e6e6"></span><span style="background:#e8a33a"></span><span style="background:#f2f2f2"></span><span style="background:#3d8fd6"></span><span style="background:#dcdcdc"></span></div>
</div>

</body>
</html>
```